Need a landing page design updated

Need an existing landing page perfected, want it too look similar to one of Quince's landing pages in that it flows and is really aesthetically pleasing. The link to the landing page is below. I need this design updated asap. Please take the content directly from the page.

http://verdantrowfl-example.com/residential-services/

Target Market(s)

High end residential landscape customers on the gulf coast of Florida (Clearwater area)

Industry/Entity Type

Landscape Gardening

Font styles to use
Sans Serif
Decorative

Requirements
Must have
• I want to keep the written content the same on on the landing page, but would like to work on making both aesthetically appealing to the consumer. This is for high end residential clients on the gulf coast of florida, so think palm trees and sunny beaches with beautiful houses and gorgeous landscapes....look through www.verdantrowfl-example.com home page for an example of the houses we landscape.
Nice to have
• Would like it to flow as you scroll similar to Quince's landing pages.
• Look at how Quince's landing page flows, want similar here.....
• https://www.quince-example.com/lumaphone-z/
Should not have
• this landing page must be beautiful and must make a lot of sense as you scroll, am looking for a work of art....please do not submit generic templates or anything that can be easily done....I need real artistry.

```html
<!DOCTYPE html>
<html lang="en">
<head>
<meta charset="utf-8">
<title>Verdant Row — Residential Landscaping</title>
<link href="https://fonts.googleapis.com/css2?family=Open+Sans:wght@300;400;600;700&family=Raleway:wght@400;500;600&display=swap" rel="stylesheet">
<style>
  :root{
    --brand:#0aa3d4;
    --brand-dark:#0d5b78;
    --brand-deep:#0b4f8c;
    --footer:#3cb6de;
    --ink:#2e2e2e;
    --muted:#5a5a5a;
    --soft:#efefef;
    --white:#ffffff;
  }
  *{box-sizing:border-box;margin:0;padding:0}
  html,body{width:1200px;height:3689px;overflow:hidden}
  body{position:relative;background:var(--white);font-family:"Open Sans",Arial,sans-serif;color:var(--ink)}
  .block{position:absolute;left:0;width:1200px}

  /* header */
  .site-header{top:0;height:91px;background:var(--white)}
  .brand{position:absolute;left:86px;top:30px;display:flex;align-items:center;gap:10px;font-family:"Open Sans",sans-serif;font-weight:600;font-size:30px;color:var(--brand-dark);letter-spacing:1px}
  .brand-dot{width:14px;height:14px;border-radius:50%;background:var(--brand)}
  .contact{position:absolute;right:30px;top:34px;text-align:right;font-size:13px;line-height:21px;color:var(--ink)}
  .contact .call{color:var(--brand)}
  .main-nav{top:91px;height:37px;background:var(--brand);display:flex;align-items:center;padding-left:93px;gap:30px}
  .main-nav a{color:var(--white);text-decoration:none;font-size:12px;font-weight:700;letter-spacing:.3px}

  /* hero */
  .hero{top:128px;height:474px;background:linear-gradient(100deg,#2f3a2e 0%,#4a5a44 40%,#7d6a5b 70%,#4d4a43 100%)}
  .hero-text{position:absolute;left:88px;top:172px;color:var(--white)}
  .hero-text h1{font-weight:400;font-size:50px;line-height:58px}
  .hero-text p{font-size:26px;line-height:34px;margin-top:6px;font-weight:400}

  .lead{top:602px;height:271px;text-align:center}
  .lead .small{margin-top:69px;font-size:19px;color:var(--ink)}
  .lead .big{font-size:22px;line-height:32px;margin-top:4px}

  .pitch{top:873px;height:147px;background:var(--soft);text-align:center}
  .pitch .small{margin-top:38px;font-size:19px}
  .pitch .big{font-size:22px;line-height:30px;margin-top:4px}

  /* comparison */
  .compare{top:1020px;height:438px;background:var(--soft)}
  .panel{position:absolute;top:0;height:438px;width:600px;color:var(--white);padding:56px 0 0 88px}
  .panel.generic{left:0;background:linear-gradient(160deg,#24b3e3 0%,#0f97c9 55%,#1aa5d2 100%)}
  .panel.tailored{left:600px;background:linear-gradient(160deg,#0f6686 0%,#0b5070 100%);padding-left:42px}
  .panel h2{font-weight:400;font-size:28px;margin-bottom:22px}
  .panel ul{list-style:none}
  .panel li{position:relative;padding-left:32px;font-size:17px;line-height:26px;margin-bottom:16px;max-width:470px}
  .panel li svg{position:absolute;left:0;top:4px}

  /* experts */
  .experts{top:1458px;height:477px}
  .experts .photo{position:absolute;left:116px;top:116px;width:400px;height:253px;background:linear-gradient(180deg,#8fb4d6 0%,#cfd9d8 40%,#5d8a3c 75%,#3f6c2a 100%)}
  .experts .copy{position:absolute;left:583px;top:132px;width:520px}
  .experts h2{font-weight:400;font-size:24px;line-height:32px;color:#444}
  .experts p{font-size:14px;line-height:25px;color:var(--muted);margin-top:12px}

  /* schedule */
  .schedule{top:1935px;height:445px;background:linear-gradient(180deg,#1b2430 0%,#22301f 60%,#2c3d1e 100%)}
  .schedule .card{position:absolute;left:150px;top:89px;width:497px;height:295px;background:var(--white);padding:64px 36px 0 36px}
  .schedule h2{font-weight:400;font-size:24px;line-height:33px}
  .schedule p{font-size:14px;line-height:24px;color:var(--muted);margin-top:18px}
  .schedule .photo{position:absolute;left:647px;top:89px;width:401px;height:295px;background:linear-gradient(135deg,#6a9a3a 0%,#9cc05a 45%,#4e7c2a 100%)}

  /* benefits */
  .benefits{top:2380px;height:480px;text-align:center}
  .benefits h2{font-family:"Raleway",sans-serif;font-weight:500;font-size:27px;margin-top:96px}
  .benefit{position:absolute;top:192px;width:290px;text-align:center}
  .benefit .icon{width:108px;height:108px;border-radius:50%;background:var(--brand);margin:0 auto;display:flex;align-items:center;justify-content:center}
  .benefit p{font-size:14px;line-height:22px;color:var(--muted);margin-top:28px}

  /* flaws */
  .flaws{top:2860px;height:342px;background:linear-gradient(180deg,#6d8f5b 0%,#4f7a30 55%,#5f9a2e 100%)}
  .flaws .overlay{position:absolute;inset:0;background:linear-gradient(120deg,#1677c4 0%,#0b59a8 60%,#0a4f96 100%);clip-path:polygon(520px 0,1200px 0,1200px 342px,640px 342px)}
  .flaws .copy{position:absolute;left:679px;top:56px;color:var(--white);width:460px}
  .flaws h2{font-weight:400;font-size:30px;line-height:38px}
  .flaws ol{margin-top:24px;padding-left:0;list-style:none;font-size:19px;line-height:28px}
  .flaws li{margin-bottom:10px;padding-left:24px;text-indent:-24px}

  /* cta */
  .cta{top:3202px;height:393px;background:#f4f4f4;text-align:center}
  .cta .q{font-family:"Raleway",sans-serif;font-size:24px;line-height:33px;margin-top:60px}
  .cta .sub{font-family:"Raleway",sans-serif;font-weight:600;font-size:20px;margin-top:12px}
  .lead-form{position:absolute;left:340px;top:216px;width:535px}
  .lead-form .field{display:block;width:535px;height:39px;border:1px solid #cfcfcf;background:var(--white);margin-bottom:11px;font-family:"Open Sans",sans-serif;font-size:12px;color:#9a9a9a;padding-left:12px;text-align:left}
  .lead-form .submit{display:block;width:142px;height:37px;background:var(--brand);color:var(--white);border:0;font-family:"Open Sans",sans-serif;font-size:12px;margin-top:-2px}

  .site-footer{top:3595px;height:94px;background:var(--footer);color:var(--white);text-align:center;font-size:15px;line-height:94px;font-weight:300}
</style>
</head>
<body>

<header class="block site-header">
  <div class="brand"><span class="brand-dot"></span>VERDANT ROW</div>
  <div class="contact">
    <div><span class="call">Call Us Now On:</span> 727-555-0148</div>
    <div>Client Portal | Get A Free Quote</div>
  </div>
</header>

<nav class="block main-nav">
  <a href="#">HOME</a><a href="#">ABOUT US</a><a href="#">RESIDENTIAL</a><a href="#">COMMERCIAL</a><a href="#">BLOG</a><a href="#">CONTACT US</a>
</nav>

<section class="block hero" role="img" aria-label="Close-up of a gardener's hand holding a green garden hose over a lawn">
  <div class="hero-text">
    <h1>Let’s guess:</h1>
    <p>You don’t have an abundance of free time. And,<br>you simply don’t want to spend the little time you have<br>– mowing a lawn and pruning the plants</p>
  </div>
</section>

<section class="block lead">
  <p class="small">You would probably like to spend that time the way you should, instead.</p>
  <p class="big">Enjoying the sunset in the privacy of your garden, watching a favorite TV show while lying<br>on a hammock, or throwing an occasional BBQ party with your friends and loved ones.</p>
</section>

<section class="block pitch">
  <p class="small">Getting an outdoor area of your dreams is not that difficult, nor expensive.</p>
  <p class="big">You can make this happen by getting a help from a landscaping company<br>that offers tailor-made services.</p>
</section>

<section class="block compare">
  <div class="panel generic" role="img" aria-label="Blue-tinted view of a palm-lined residential driveway">
    <h2>Generic landscaping services:</h2>
    <ul>
      <li><svg width="18" height="18" viewBox="0 0 18 18"><circle cx="9" cy="9" r="9" fill="#fff"/><path d="M5 9.5l2.6 2.6L13 6.6" fill="none" stroke="#15a0d2" stroke-width="2"/></svg>You pay for the bundle of services, regardless of whether you actually need them</li>
      <li><svg width="18" height="18" viewBox="0 0 18 18"><circle cx="9" cy="9" r="9" fill="#fff"/><path d="M5 9.5l2.6 2.6L13 6.6" fill="none" stroke="#15a0d2" stroke-width="2"/></svg>You get a generic service, not adjusted to the specific needs of your outdoor area</li>
      <li><svg width="18" height="18" viewBox="0 0 18 18"><circle cx="9" cy="9" r="9" fill="#fff"/><path d="M5 9.5l2.6 2.6L13 6.6" fill="none" stroke="#15a0d2" stroke-width="2"/></svg>The field team thinks of your property as just another task they have to complete</li>
    </ul>
  </div>
  <div class="panel tailored">
    <h2>Tailor-made landscaping services:</h2>
    <ul>
      <li><svg width="18" height="18" viewBox="0 0 18 18"><circle cx="9" cy="9" r="9" fill="#fff"/><path d="M5 9.5l2.6 2.6L13 6.6" fill="none" stroke="#0d5b78" stroke-width="2"/></svg>You pay only for the services your yard really needs.</li>
      <li><svg width="18" height="18" viewBox="0 0 18 18"><circle cx="9" cy="9" r="9" fill="#fff"/><path d="M5 9.5l2.6 2.6L13 6.6" fill="none" stroke="#0d5b78" stroke-width="2"/></svg>You get your garden’s specific issues solved, and specific requirements met</li>
      <li><svg width="18" height="18" viewBox="0 0 18 18"><circle cx="9" cy="9" r="9" fill="#fff"/><path d="M5 9.5l2.6 2.6L13 6.6" fill="none" stroke="#0d5b78" stroke-width="2"/></svg>The field team members take their time<br>working on your property</li>
      <li><svg width="18" height="18" viewBox="0 0 18 18"><circle cx="9" cy="9" r="9" fill="#fff"/><path d="M5 9.5l2.6 2.6L13 6.6" fill="none" stroke="#0d5b78" stroke-width="2"/></svg>They get to learn all about your vision –<br>and make it a reality</li>
    </ul>
  </div>
</section>

<section class="block experts">
  <div class="photo" role="img" aria-label="White two-storey house with a manicured lawn and flowering trees"></div>
  <div class="copy">
    <h2>Why should you care that Verdant Row employs the leading industry experts and uses modern, eco-friendly technical solutions?</h2>
    <p>That is why we’re able to transform your lawn into a green carpet and get your plants in a perfect health. All while keeping your vision and your budget on our minds. That is why our services actually enable you to reduce the operating expenses.</p>
  </div>
</section>

<section class="block schedule" role="img" aria-label="Dusk view of a garden lawn with trees">
  <div class="card">
    <h2>Do you worry our services are going to disturb you while trying to unwind in the privacy of your own garden?</h2>
    <p>Our Client Service Operators Build A Schedule Around Your Needs –Designed Not To Disturb You At All.</p>
  </div>
  <div class="photo" role="img" aria-label="Person relaxing on green grass among white flowers"></div>
</section>

<section class="block benefits">
  <h2>More benefits of having a well-maintained yard:</h2>
  <div class="benefit" style="left:106px">
    <div class="icon"><svg width="52" height="44" viewBox="0 0 52 44"><path d="M3 3v38h46" fill="none" stroke="#fff" stroke-width="4"/><path d="M10 32l11-12 8 8 14-16" fill="none" stroke="#fff" stroke-width="4"/><path d="M36 10h9v9" fill="none" stroke="#fff" stroke-width="4"/></svg></div>
    <p>In some cases, a great-looking<br>lawn can increase your property’s<br>value up to 20%.</p>
  </div>
  <div class="benefit" style="left:445px">
    <div class="icon"><svg width="54" height="50" viewBox="0 0 54 50"><path d="M4 24L27 4l23 20" fill="none" stroke="#fff" stroke-width="4"/><path d="M10 20v27h34V20" fill="none" stroke="#fff" stroke-width="4"/><circle cx="27" cy="32" r="9" fill="none" stroke="#fff" stroke-width="3"/><text x="27" y="37" font-family="Open Sans,sans-serif" font-size="13" font-weight="700" fill="#fff" text-anchor="middle">$</text></svg></div>
    <p>Your lawn and plants reduce the<br>energy consumption – countering the<br>warming effects of paved surfaces.</p>
  </div>
  <div class="benefit" style="left:780px">
    <div class="icon"><svg width="54" height="40" viewBox="0 0 54 40"><rect x="2" y="8" width="22" height="24" fill="none" stroke="#fff" stroke-width="4"/><path d="M18 20h26" stroke="#fff" stroke-width="6"/><path d="M38 8l14 12-14 12z" fill="#fff"/></svg></div>
    <p>They act as giant dust filters, increas-<br>ing air quality, and removing carbon<br>dioxide from the atmosphere</p>
  </div>
</section>

<section class="block flaws" role="img" aria-label="Wooden garden table and chairs on a lawn beside purple flower beds">
  <div class="overlay"></div>
  <div class="copy">
    <h2>Do our services have flaws?<br>Yes. They have two giant ones.</h2>
    <ol>
      <li>1. Your “new” garden will get all of your neighbors jealous.</li>
      <li>2. Your friends will probably start inviting themselves over more frequently.</li>
    </ol>
  </div>
</section>

<section class="block cta">
  <p class="q">So, what’s the next step to enriching your living area?<br>And getting you a garden from your dreams.</p>
  <p class="sub">It’s simple, just book a no-obligations consultation</p>
  <form class="lead-form">
    <input class="field" type="text" placeholder="Name">
    <input class="field" type="text" placeholder="Phone OR Email">
    <button class="submit" type="button">Get Started</button>
  </form>
</section>

<footer class="block site-footer">Copyright 2017 Verdant Row All Rights Reserved</footer>

</body>
</html>
```